NEW Wordpress Website Design for a Dynamic Long Term Healthcare Company in Hawaii

I would like a new website design for my current company, Marlowe Kin Partners, which has two different brands - Marlowe Homecare and Marlowe Senior Living. You can see the current website at www.marlowekin.example. The website should be built using Wordpress Software and the Elementor theme. The website should have a local Hawaii island/tropical feel, but look professional for healthcare. I'm looking for something fresh, and want the designer to select colors, styles, etc.

In the Header, on all pages, I would like a menu that includes Home Care, Senior Living, Rates, and About Us.
Under each of the Header Menu Titles, I would like these drop downs included:
Home Care (drop down pages)- Nurse Aide Care, 24-Hour Home Care, Skilled Nursing, Lifestyle Aide, Hospice at Home, Bathing & Meal Service.
Senior Living (drop down pages) - Long-Term Stay, Short-Term Stay.
Rates (drop down page) - Rates.
About Us (drop down pages) - Our Mission, Porch Chats, About Dana Marlowe.

In the footer, on all pages, you should include the address: 238 Pueo Ridge Rd, Suite 120, Honolulu, HI 96822. Phone number: 808-555-0173
The footer should also include buttons for a page called Learn, Caregiver Jobs, and each of the service page links to include: Nurse Aide Care, 24-Hour Home Care, Skilled Nursing, Lifestyle Aide, Hospice at Home, Bathing & Meal Service.
Please don't take the current website and redesign a few aspects. I'm looking for a completely different look and feel.

Target Market(s)

40-80 year olds

Industry/Entity Type

Long Term Healthcare

Coding

Coded - Design and coding required

Requirements
Should not have
• Our existing website as a template. We are looking for a complete redesign. Thank you.

```html
<!DOCTYPE html>
<html lang="en">
<head>
<meta charset="utf-8">
<title>Marlowe Kin Partners — Homecare &amp; Senior Living</title>
<link rel="stylesheet" href="https://fonts.googleapis.com/css2?family=Poppins:ital,wght@0,300;0,400;0,500;0,600;0,700;0,800;1,600&display=swap">
<style>
:root{
  --teal:#5a9893;
  --teal-dark:#4f8b86;
  --coral:#f2857a;
  --mint:#a8cbb5;
  --mist:#eef3f3;
  --ink:#222;
  --body:#555;
  --white:#fff;
}
*{box-sizing:border-box;margin:0;padding:0}
html,body{width:1200px;height:3917px;overflow:hidden}
body{position:relative;font-family:'Poppins',sans-serif;background:var(--white);color:var(--ink)}
.abs{position:absolute}
.btn{position:absolute;display:flex;align-items:center;justify-content:center;height:52px;border-radius:26px;
  background:linear-gradient(90deg,var(--coral) 0%,#d98a80 45%,var(--teal) 100%);color:#fff;font-size:15px;font-weight:500;letter-spacing:.2px}
/* top bar */
.topbar{left:0;top:0;width:1200px;height:38px;background:var(--teal);display:flex;justify-content:flex-end;align-items:center;gap:26px;padding-right:74px}
.topbar .call{display:flex;align-items:center;gap:9px;color:#fff;font-size:11px}
.topbar .ring{width:24px;height:24px;border:1.5px solid #fff;border-radius:50%;display:flex;align-items:center;justify-content:center}
/* header */
.header{left:0;top:38px;width:1200px;height:114px;background:#fff}
.brand{position:absolute;display:flex;align-items:center;gap:6px;font-size:14px;font-weight:600;line-height:1.1}
.brand .dot{width:14px;height:14px;border-radius:50%}
.nav{position:absolute;right:66px;top:48px;display:flex;gap:28px;font-size:15px;font-weight:500;color:#222}
.nav span{display:flex;align-items:center;gap:8px}
/* hero */
.hero{left:0;top:152px;width:1200px;height:593px;overflow:hidden}
.hero-photo{position:absolute;inset:0;background:linear-gradient(100deg,#4d3a2a 0%,#6e5238 35%,#8a6c4c 55%,#6a5a48 80%,#4a4036 100%)}
.hero-shade{position:absolute;inset:0;background:linear-gradient(90deg,rgba(0,0,0,.35),rgba(0,0,0,0) 60%)}
.hero h1{position:absolute;left:106px;top:66px;font-size:42px;font-weight:800;color:#fff;line-height:52px;text-transform:uppercase}
.hero p{position:absolute;left:106px;top:186px;width:540px;font-size:17px;line-height:27px;color:#fff}
.hero p b{font-weight:600}
.hero svg{position:absolute;left:0;bottom:0}
/* services */
.section-title{position:absolute;font-size:40px;font-weight:800;color:var(--teal);text-transform:uppercase}
.band{left:0;top:1431px;width:1200px;height:125px;background:var(--mist)}
.card-photo{position:absolute;width:473px;height:297px;border-radius:10px}
.card-title{position:absolute;width:480px;font-size:27px;font-weight:600;line-height:36px;color:#111}
.card-text{position:absolute;width:480px;font-size:14.5px;line-height:24.5px;color:var(--body)}
/* consultation */
.consult-photo{left:0;top:1556px;width:600px;height:659px;background:linear-gradient(160deg,#4f7a3c 0%,#7ea35a 40%,#b9b7a6 75%,#d6d2c8 100%)}
.consult{left:600px;top:1556px;width:600px;height:659px;background:var(--teal)}
.consult h2{position:absolute;left:75px;top:34px;font-size:30px;font-weight:700;line-height:43px;color:#fff;text-transform:uppercase}
.field{position:absolute;left:75px;width:449px;height:52px;border-radius:26px;background:#fff;font-size:15px;color:#333;padding-left:28px;display:flex;align-items:center}
.consult .note{position:absolute;left:103px;top:524px;width:400px;font-size:10.5px;line-height:16px;color:#fff}
.consult .submit{position:absolute;left:75px;top:569px;width:449px;height:52px;border-radius:26px;background:var(--coral);color:#fff;font-weight:600;font-size:14px;display:flex;align-items:center;justify-content:center}
/* about */
.about-bg{left:0;top:2215px;width:1200px;height:1180px;background:var(--mist)}
.about-photo{left:106px;top:2388px;width:420px;height:444px;border-radius:4px;background:linear-gradient(160deg,#d9d3cb 0%,#c8b9a8 50%,#e9e6e2 100%);box-shadow:0 6px 18px rgba(0,0,0,.15)}
.about-text{left:580px;top:2404px;width:510px;font-size:15px;line-height:24.5px;color:var(--body)}
.about-text p+p{margin-top:24px}
.quote{left:0;top:3058px;width:1200px;text-align:center;font-size:33px;font-weight:600;font-style:italic;line-height:42px;color:var(--teal)}
/* footer */
.footer{left:0;top:3285px;width:1200px;height:632px}
.footer-brand{left:160px;top:3480px;display:flex;align-items:center;gap:10px;color:#fff;font-size:20px;font-weight:600}
.footer-brand .sq{width:22px;height:22px;background:#fff;border-radius:3px}
.contact{position:absolute;left:160px;display:flex;align-items:center;gap:16px;color:#fff;font-size:15px;line-height:23px}
.contact .ic{width:34px;height:34px;border-radius:50%;background:rgba(255,255,255,.25);display:flex;align-items:center;justify-content:center;flex:none}
.fcol{position:absolute;top:3472px;color:#fff}
.fcol h4{font-size:15px;font-weight:700;letter-spacing:.3px;margin-bottom:13px}
.fcol li{list-style:none;font-size:15px;line-height:32px}
.copyright{left:160px;top:3803px;color:#fff;font-size:13px}
.social{left:898px;top:3805px;display:flex;gap:28px}
.social span{width:12px;height:12px;border-radius:50%;background:#fff;display:block}
</style>
</head>
<body>

<div class="abs topbar">
  <div class="call"><span class="ring"><svg width="11" height="11" viewBox="0 0 24 24"><path fill="#fff" d="M6.6 10.8a15 15 0 0 0 6.6 6.6l2.2-2.2a1 1 0 0 1 1-.25 11.4 11.4 0 0 0 3.6.6 1 1 0 0 1 1 1V20a1 1 0 0 1-1 1A17 17 0 0 1 3 4a1 1 0 0 1 1-1h3.5a1 1 0 0 1 1 1c0 1.25.2 2.45.6 3.6a1 1 0 0 1-.25 1z"/></svg></span>CALL (808) 555-0173</div>
  <div class="call"><span class="ring"><svg width="11" height="11" viewBox="0 0 24 24"><path fill="#fff" d="M6.6 10.8a15 15 0 0 0 6.6 6.6l2.2-2.2a1 1 0 0 1 1-.25 11.4 11.4 0 0 0 3.6.6 1 1 0 0 1 1 1V20a1 1 0 0 1-1 1A17 17 0 0 1 3 4a1 1 0 0 1 1-1h3.5a1 1 0 0 1 1 1c0 1.25.2 2.45.6 3.6a1 1 0 0 1-.25 1z"/></svg></span>CALL (808) 555-0173</div>
</div>

<header class="abs header">
  <div class="brand" style="left:96px;top:40px;color:var(--coral)"><span class="dot" style="background:var(--coral)"></span>Marlowe<br>Homecare</div>
  <div class="brand" style="left:196px;top:40px;color:var(--teal)"><span class="dot" style="background:var(--teal)"></span>Marlowe<br>Senior Living</div>
  <nav class="nav">
    <span>Home Care <svg width="10" height="6" viewBox="0 0 10 6"><path d="M1 1l4 4 4-4" stroke="#222" stroke-width="1.5" fill="none"/></svg></span>
    <span>Senior Living <svg width="10" height="6" viewBox="0 0 10 6"><path d="M1 1l4 4 4-4" stroke="#222" stroke-width="1.5" fill="none"/></svg></span>
    <span>Rates</span>
    <span>About Us <svg width="10" height="6" viewBox="0 0 10 6"><path d="M1 1l4 4 4-4" stroke="#222" stroke-width="1.5" fill="none"/></svg></span>
  </nav>
</header>

<section class="abs hero">
  <div class="hero-photo" role="img" aria-label="Photo of a caregiver and a smiling client sitting together on a sofa in a warm living room"></div>
  <div class="hero-shade"></div>
  <h1>Hawaii's Choice<br>Homecare &amp; Senior Living</h1>
  <p><b>Marlowe Homecare</b> provides a variety of professional in-home health care services throughout the entire island of Oahu. <b>Marlowe Senior Living</b>, a beautiful Adult Residential Care Home, is located on the windward side of Oahu in Kailua.</p>
  <div class="btn" style="left:106px;top:326px;width:148px">LEARN MORE</div>
  <svg width="1200" height="180" viewBox="0 0 1200 180">
    <path fill="var(--teal)" d="M300,45 C420,10 520,30 700,110 C820,160 950,175 1080,150 C950,190 820,180 700,140 C540,80 430,50 300,45 Z"/>
    <path fill="#fff" d="M0,180 C120,90 210,50 330,45 C480,45 600,120 740,160 C860,190 1000,180 1200,150 L1200,180 Z"/>
  </svg>
</section>

<h2 class="section-title" style="left:135px;top:763px">Our Services</h2>
<div class="abs band"></div>

<div class="card-photo" style="left:106px;top:876px;background:linear-gradient(150deg,#c8c46a 0%,#e1dc8c 45%,#8a6a4c 100%)" role="img" aria-label="Photo of a caregiver helping an older man sitting on a bed"></div>
<div class="card-photo" style="left:619px;top:876px;background:linear-gradient(150deg,#7a3a26 0%,#a86a44 40%,#d2c98a 75%,#8ea860 100%)" role="img" aria-label="Photo of a caregiver serving a meal to two residents at a dining table"></div>

<h3 class="card-title" style="left:106px;top:1201px">Home Care - Professional Care In Your Home</h3>
<h3 class="card-title" style="left:619px;top:1201px">Senior Living - Trusted Care In Our Home</h3>
<p class="card-text" style="left:106px;top:1285px">Marlowe Homecare understands that every person's care journey is unique. We tailor our in-home services to meet the diverse nurturing experience of professional quality care and safety within the comfort and convenience of your own home.</p>
<p class="card-text" style="left:619px;top:1285px">Marlowe Homecare understands that every person's care journey is unique. We tailor our in-home services to meet the diverse nurturing experience of professional quality care and safety within the comfort and convenience of your own home.</p>
<div class="btn" style="left:106px;top:1411px;width:273px;font-size:14px">SCHEDULE CARE ASSESSMENT</div>
<div class="btn" style="left:619px;top:1411px;width:173px;font-size:14px">SCHEDULE TOUR</div>

<div class="abs consult-photo" role="img" aria-label="Photo of a caregiver helping a woman walk with a walker along a tropical garden path"></div>
<section class="abs consult">
  <h2>Schedule a Complimentary<br>Care Consultation</h2>
  <div class="field" style="top:141px">Name *</div>
  <div class="field" style="top:205px">Email *</div>
  <div class="field" style="top:269px">Phone *</div>
  <div class="field" style="top:333px">How can we help you?</div>
  <div class="field" style="top:397px">Questions/Comments</div>
  <div class="field" style="top:461px">May we email you about this?</div>
  <p class="note"><b>Note</b> : You agree to receive future emails and understand you may opt-out at any time</p>
  <div class="submit">SUBMIT</div>
</section>

<div class="abs about-bg"></div>
<h2 class="section-title" style="left:0;width:1200px;text-align:center;top:2287px">About Us</h2>
<div class="abs about-photo" role="img" aria-label="Portrait photo of a smiling nurse wearing a stethoscope"></div>
<div class="abs about-text">
  <p>At Marlowe Kin Partners, our mission is to provide compassionate and professional long-term healthcare services that empower individuals to maintain their highest level of independence, health, and well-being in the comfort of their own homes or ours, either through our licensed home healthcare agency - Marlowe Homecare, or in our Adult Residential Care Home - Marlowe Senior Living.</p>
  <p>We are dedicated to delivering personalized care that addresses the unique needs of each client, fostering a sense of trust, respect, and dignity. Our team of skilled healthcare professionals is committed to creating a supportive environment that not only attends to medical needs but also promotes emotional and social well-being.</p>
</div>
<div class="btn" style="left:580px;top:2761px;width:148px">LEARN MORE</div>

<div class="abs" style="left:576px;top:2975px;width:48px;height:48px;border-radius:50%;background:linear-gradient(135deg,var(--coral),var(--teal))"></div>
<p class="abs quote">“Caregiving is a series of small acts of care that<br>alter the course of someone's life”</p>

<footer class="abs footer">
  <svg width="1200" height="632" viewBox="0 0 1200 632" style="position:absolute;left:0;top:0">
    <path fill="var(--teal)" d="M0,55 C180,-10 330,0 520,60 C700,115 870,190 1200,80 L1200,632 L0,632 Z"/>
    <path fill="#fff" d="M0,55 C180,-10 330,0 520,60 C700,115 870,190 1200,80 L1200,92 C870,200 700,128 520,72 C330,12 180,2 0,70 Z"/>
    <path fill="var(--mint)" d="M250,10 C420,-5 560,40 700,90 C830,135 960,150 1080,125 C960,165 830,150 700,110 C560,65 420,20 250,10 Z"/>
  </svg>
</footer>

<div class="abs footer-brand"><span class="sq"></span>Marlowe Kin Partners</div>

<div class="contact" style="top:3602px"><span class="ic"><svg width="12" height="15" viewBox="0 0 12 16"><path fill="#fff" d="M6 0a6 6 0 0 0-6 6c0 4.5 6 10 6 10s6-5.5 6-10a6 6 0 0 0-6-6zm0 8.2A2.2 2.2 0 1 1 6 3.8a2.2 2.2 0 0 1 0 4.4z"/></svg></span><span>238 Pueo Ridge Rd, Suite 120,<br>Honolulu, HI 96822</span></div>
<div class="contact" style="top:3668px"><span class="ic"><svg width="13" height="13" viewBox="0 0 24 24"><path fill="#fff" d="M6.6 10.8a15 15 0 0 0 6.6 6.6l2.2-2.2a1 1 0 0 1 1-.25 11.4 11.4 0 0 0 3.6.6 1 1 0 0 1 1 1V20a1 1 0 0 1-1 1A17 17 0 0 1 3 4a1 1 0 0 1 1-1h3.5a1 1 0 0 1 1 1c0 1.25.2 2.45.6 3.6a1 1 0 0 1-.25 1z"/></svg></span><span>(808)-555-0173</span></div>

<div class="fcol" style="left:572px">
  <h4>PAGES</h4>
  <ul><li>Home</li><li>About Us</li><li>Learn</li><li>Caregiver Jobs</li></ul>
</div>
<div class="fcol" style="left:867px">
  <h4>SERVICES</h4>
  <ul><li>Nurse Aide Care</li><li>24-Hour Home Care</li><li>Skilled Nursing</li><li>Lifestyle Aide</li><li>Hospice at Home</li><li>Bathing &amp; Meal Service</li></ul>
</div>

<p class="abs copyright">© 2023 Marlowe Kin Partners. All Rights Reserved.</p>
<div class="abs social" aria-label="Social links"><span></span><span></span><span></span><span></span></div>

</body>
</html>
```